Small rum distillery looking for bottle design

Small rum distillery in Estonia. Looking for bottle lable design. It should be simple but at the same time point out from the variety of other bottles.
As we are a small nordic country, design can be some how nordic or represent our country. It can also have some connection with sailing or sea as we know it pirates love it.
Bottle we are using is Corvane 540

Industry/Entity Type

food and beverage

Other font styles liked:
• Baskerville

```html
<!DOCTYPE html>
<html lang="en">
<head>
<meta charset="utf-8">
<title>Haldra Distillery – Tidemark Rum Label</title>
<link rel="stylesheet" href="https://fonts.googleapis.com/css2?family=Cormorant+Garamond:wght@500;600&family=Rye&family=Mr+Dafoe&display=swap">
<style>
  :root {
    --page: #ffffff;
    --ink: #3a3a3c;
    --ink-soft: #4a4a4d;
    --rum-red: #a8202a;
    --band-red: #8f1d22;
    --band-dark: #6e1418;
    --label-cream: #ece3d4;
    --label-light: #f4eee4;
    --map-tone: #d9ccb8;
    --ornament: #f7f2ea;
    --band-text: #f4ece0;
  }
  * { box-sizing: border-box; margin: 0; padding: 0; }
  html, body {
    width: 1200px;
    height: 1180px;
    overflow: hidden;
    background: var(--page);
  }
  .canvas {
    position: relative;
    width: 1200px;
    height: 1180px;
    background: var(--page);
  }

  /* Brand sign-off */
  .brand-lockup {
    position: absolute;
    top: 70px;
    left: 0;
    width: 1200px;
    display: flex;
    align-items: center;
    justify-content: center;
    gap: 18px;
  }
  .brand-dot {
    width: 34px;
    height: 34px;
    border-radius: 50%;
    background: var(--rum-red);
  }
  .brand-name {
    font-family: "Cormorant Garamond", serif;
    font-weight: 500;
    font-size: 56px;
    letter-spacing: 6px;
    color: var(--ink);
  }

  /* Label */
  .label {
    position: absolute;
    top: 190px;
    left: 110px;
    width: 980px;
    height: 920px;
    background: var(--label-cream);
    overflow: hidden;
  }
  .label-map {
    position: absolute;
    inset: 0 0 150px 0;
    background:
      radial-gradient(ellipse at 15% 30%, var(--map-tone) 0%, transparent 45%),
      radial-gradient(ellipse at 88% 20%, var(--map-tone) 0%, transparent 40%),
      radial-gradient(ellipse at 85% 80%, var(--map-tone) 0%, transparent 40%),
      radial-gradient(ellipse at 10% 85%, var(--map-tone) 0%, transparent 40%),
      var(--label-cream);
  }
  .label-ornament {
    position: absolute;
    left: 50%;
    top: 50px;
    width: 820px;
    height: 820px;
    margin-left: -410px;
    border-radius: 50%;
    background: radial-gradient(circle, var(--label-light) 0%, var(--label-light) 52%, var(--ornament) 53%, var(--label-cream) 72%);
  }
  .label-content {
    position: absolute;
    top: 215px;
    left: 0;
    width: 100%;
    text-align: center;
  }
  .label-brand {
    display: inline-flex;
    align-items: center;
    gap: 12px;
    padding-bottom: 8px;
    border-bottom: 2px solid var(--ink-soft);
  }
  .label-brand .brand-dot { width: 22px; height: 22px; }
  .label-brand .brand-name { font-size: 42px; letter-spacing: 4px; }
  .product-name {
    margin-top: 20px;
    font-family: "Rye", serif;
    font-size: 108px;
    line-height: 1;
    color: var(--ink);
  }
  .product-type {
    margin-top: 14px;
    font-family: "Rye", serif;
    font-size: 84px;
    line-height: 1;
    color: var(--rum-red);
  }
  .tagline {
    margin-top: 18px;
    font-family: "Mr Dafoe", cursive;
    font-size: 40px;
    color: var(--ink-soft);
  }
  .ship-medallion {
    display: block;
    margin: 22px auto 0;
    width: 200px;
    height: 200px;
    border-radius: 50%;
    border: 5px solid var(--ink-soft);
    background: radial-gradient(circle, #e6ddd0 0%, #cfc4b4 70%, #b8ad9d 100%);
  }

  /* Bottom band */
  .label-band {
    position: absolute;
    left: 0;
    bottom: 66px;
    width: 100%;
    height: 62px;
    background: linear-gradient(90deg, var(--band-dark), var(--band-red) 20%, var(--band-red) 80%, var(--band-dark));
    border-top: 6px solid var(--label-light);
    display: flex;
    align-items: center;
    justify-content: center;
    font-family: "Cormorant Garamond", serif;
    font-weight: 600;
    font-size: 28px;
    letter-spacing: 1px;
    color: var(--band-text);
  }
  .label-foot {
    position: absolute;
    left: 0;
    bottom: 0;
    width: 100%;
    height: 66px;
    background: var(--label-light);
  }
</style>
</head>
<body>
  <main class="canvas">
    <header class="brand-lockup">
      <span class="brand-dot"></span>
      <span class="brand-name">HALDRA DISTILLERY</span>
    </header>

    <section class="label">
      <div class="label-map" role="img" aria-label="Engraved old-style map of a northern coastline with forests, mountains and a castle tower"></div>
      <div class="label-ornament" role="img" aria-label="Interlaced Nordic knot ornament framing the centre of the label"></div>

      <div class="label-content">
        <div class="label-brand">
          <span class="brand-dot"></span>
          <span class="brand-name">HALDRA</span>
        </div>
        <h1 class="product-name">TIDEMARK</h1>
        <h2 class="product-type">DISTILLERY</h2>
        <p class="tagline">High Quality Rum</p>
        <div class="ship-medallion" role="img" aria-label="Round engraved medallion of a three-masted sailing ship on the sea inside a rope border"></div>
      </div>

      <div class="label-band">750ML | 13.4% ALC/VOL | ESTONIA</div>
      <div class="label-foot"></div>
    </section>
  </main>
</body>
</html>
```